Website For Custom Home Builder

-Very elegant and simple design as I am a high end custom home builder.
-I build homes $2 million to $10 million range so the website needs to reflect the level of home that I build.
-Attached are photos of homes I have built to use as well as my logo.
-I need final design to be in layered format so my local guy can edit if he needs to.

3 Page Design
1. HomePage:
-logo, some photos,
-“Building beautiful custom homes in Indianapolis for over 20 years”
2. AboutPage:
-Wade Holloran has been building stunning custom homes in the Indianpolis area for over 20 years. As a small boutique building company we only build a handful of homes a year in order to offer our clients the personal attention that their homes deserve. It's this attention to detail that makes our client experience and final product something special and unique.
- family photo
3. ContactPage:
-office photo
-317-552-7190
-wade@whcrafted.com
-415 North Fernmill Rd, Suite 308, Carmel IN 46033

Target Market(s)

Very high end clients looking to build $2 million to $10 million homes.

Industry/Entity Type

Residential high end custom home builder/construction

Coding

Coded - Design and coding required

Number of Pages Required

3 page

Requirements
Must have
• Very simple and elegant design that represents the high end homes that I build.
Nice to have
Should not have
• Should NOT have a lot of clutter or be a very busy page from a design perspective.

```html
<!DOCTYPE html>
<html lang="en">
<head>
<meta charset="utf-8">
<title>Wade Holloran Custom Homes</title>
<link rel="stylesheet" href="https://fonts.googleapis.com/css2?family=Jost:wght@400;500&family=Playfair+Display:wght@400&family=Cormorant+Garamond:wght@500;600&family=Mulish:wght@400&display=swap">
<style>
  :root {
    --sidebar: #131313;
    --sidebar-active: #222222;
    --divider: #2c2c2c;
    --white: #ffffff;
    --ink: #141414;
    --accent: #d97a30;
    --accent-deep: #b2622a;
    --hero-light: #f4f4f4;
  }
  * { margin: 0; padding: 0; box-sizing: border-box; }
  html, body { width: 1200px; height: 585px; overflow: hidden; background: var(--white); }
  .page { position: relative; width: 1200px; height: 585px; overflow: hidden; }

  .sidebar {
    position: absolute; left: 0; top: 0; width: 196px; height: 585px;
    background: var(--sidebar); color: var(--white);
    font-family: "Jost", sans-serif;
  }
  .brand {
    position: absolute; top: 66px; left: 0; width: 196px; text-align: center;
    font-family: "Jost", sans-serif; font-weight: 400; font-size: 18px;
    letter-spacing: 0.3px; color: var(--white); line-height: 1.1;
  }
  .nav { position: absolute; top: 177px; left: 0; width: 196px; list-style: none; }
  .nav-item {
    height: 71px; display: flex; align-items: center; padding-left: 30px;
    border-bottom: 1px solid var(--divider);
    font-weight: 500; font-size: 16.5px; letter-spacing: 0.3px; text-transform: uppercase;
  }
  .nav-item:last-child { border-bottom: none; }
  .nav-item.is-active { background: var(--sidebar-active); color: var(--accent); }
  .nav-icon { width: 28px; height: 28px; margin-right: 12px; flex: none; }
  .follow {
    position: absolute; left: 30px; top: 478px;
    font-weight: 500; font-size: 14.5px; letter-spacing: 0.3px;
  }
  .social { position: absolute; left: 30px; top: 516px; display: flex; gap: 10px; }
  .social-dot {
    width: 36px; height: 36px; border-radius: 50%;
    border: 1px solid #2e2e2e; background: var(--sidebar);
    display: flex; align-items: center; justify-content: center; color: var(--white);
  }
  .social-dot svg { width: 14px; height: 14px; }
  .social-dot.is-primary { background: var(--accent-deep); border-color: var(--accent-deep); }

  .hero-backdrop {
    position: absolute; left: 196px; top: 0; width: 425px; height: 585px;
    background: linear-gradient(160deg, #ececec 0%, var(--hero-light) 45%, #fafafa 100%);
  }
  .hero-copy { position: absolute; left: 225px; top: 191px; color: var(--ink); }
  .hero-kicker {
    font-family: "Cormorant Garamond", serif; font-weight: 600; font-size: 12.5px;
    letter-spacing: 1.4px; text-transform: uppercase;
  }
  .hero-title {
    font-family: "Playfair Display", serif; font-weight: 400; font-size: 53px;
    line-height: 1; margin-top: 10px; letter-spacing: -0.3px;
  }
  .hero-sub {
    font-family: "Cormorant Garamond", serif; font-weight: 600; font-size: 21px;
    margin-top: 10px;
  }
  .hero-sub .highlight { color: var(--accent); }
  .cta {
    display: inline-flex; align-items: center; justify-content: center;
    margin-top: 33px; width: 156px; height: 50px;
    background: var(--accent); color: var(--white);
    font-family: "Jost", sans-serif; font-size: 14px; letter-spacing: 0.3px;
    border-radius: 2px;
  }

  .showcase {
    position: absolute; left: 621px; top: 0; width: 579px; height: 500px;
    background:
      radial-gradient(ellipse 220px 260px at 88% 42%, rgba(214,140,60,0.55), rgba(214,140,60,0) 70%),
      linear-gradient(90deg, rgba(20,20,18,0.35) 0%, rgba(20,20,18,0) 45%, rgba(60,40,25,0.25) 100%),
      linear-gradient(180deg, #6e4e36 0%, #b36f34 16%, #8a6040 30%, #4a4036 46%, #34404a 60%, #8a7e70 72%, #54452e 84%, #4a4a28 100%);
  }
  .footer {
    position: absolute; left: 621px; top: 500px; width: 579px; height: 85px;
    background: var(--white); display: flex; align-items: center; justify-content: center;
    font-family: "Mulish", sans-serif; font-size: 13.5px; color: var(--ink);
  }
  .footer .highlight { color: var(--accent); }
</style>
</head>
<body>
<div class="page">
  <aside class="sidebar">
    <div class="brand">WADE HOLLORAN</div>
    <ul class="nav">
      <li class="nav-item is-active">
        <svg class="nav-icon" viewBox="0 0 28 28" fill="none" stroke="currentColor" stroke-width="1.6" stroke-linejoin="round">
          <path d="M3 13 L14 3 L25 13"/><path d="M6 11 V25 H22 V11"/><path d="M11 25 V17 H17 V25"/>
        </svg>
        <span>Home</span>
      </li>
      <li class="nav-item">
        <svg class="nav-icon" viewBox="0 0 28 28" fill="none" stroke="currentColor" stroke-width="1.6">
          <circle cx="14" cy="9" r="6"/><path d="M3 26 C3 19 8 16 14 16 C20 16 25 19 25 26 Z"/>
        </svg>
        About Us
      </li>
      <li class="nav-item">
        <svg class="nav-icon" viewBox="0 0 28 28" fill="none" stroke="currentColor" stroke-width="1.6" stroke-linejoin="round">
          <path d="M5 3 H10 L12 9 L9 11 C10 15 13 18 17 19 L19 16 L25 18 V23 C25 24 24 25 23 25 C12 25 3 16 3 5 C3 4 4 3 5 3 Z"/>
          <circle cx="20" cy="7" r="4.5"/><path d="M20 5 V7.5 H21.5"/>
        </svg>
        Contact Us
      </li>
    </ul>
    <div class="follow">FOLLOW US</div>
    <div class="social">
      <span class="social-dot is-primary" role="img" aria-label="Social profile link">
        <svg viewBox="0 0 14 14" fill="none" stroke="currentColor" stroke-width="1.6" stroke-linecap="round"><path d="M6 8 L8 6"/><path d="M5 6.5 L3.5 8 A2 2 0 0 0 6 10.5 L7.5 9"/><path d="M9 7.5 L10.5 6 A2 2 0 0 0 8 3.5 L6.5 5"/></svg>
      </span>
      <span class="social-dot" role="img" aria-label="Social profile link">
        <svg viewBox="0 0 14 14" fill="none" stroke="currentColor" stroke-width="1.6" stroke-linecap="round"><path d="M6 8 L8 6"/><path d="M5 6.5 L3.5 8 A2 2 0 0 0 6 10.5 L7.5 9"/><path d="M9 7.5 L10.5 6 A2 2 0 0 0 8 3.5 L6.5 5"/></svg>
      </span>
      <span class="social-dot" role="img" aria-label="Social profile link">
        <svg viewBox="0 0 14 14" fill="none" stroke="currentColor" stroke-width="1.6" stroke-linecap="round"><path d="M6 8 L8 6"/><path d="M5 6.5 L3.5 8 A2 2 0 0 0 6 10.5 L7.5 9"/><path d="M9 7.5 L10.5 6 A2 2 0 0 0 8 3.5 L6.5 5"/></svg>
      </span>
    </div>
  </aside>

  <div class="hero-backdrop" role="img" aria-label="Soft faded photo of a bright living room with tall windows"></div>
  <section class="hero-copy">
    <p class="hero-kicker">Building Beautiful</p>
    <h1 class="hero-title">Custom Homes</h1>
    <p class="hero-sub">in Indianapolis for over <span class="highlight">20 years</span></p>
    <a class="cta">GET STARTED</a>
  </section>

  <div class="showcase" role="img" aria-label="Photo of a luxury stone home with a lit pool terrace at sunset"></div>
  <footer class="footer">
    <p>Copyright © 2023 <span class="highlight">Wade Holloran</span>. All Rights Reserved.</p>
  </footer>
</div>
</body>
</html>
```